Personal Brand Business Card

I am looking for a design that I will use as my personal brand that conveys class (think 1920s gentlemen) and is timeless. I will be putting this on a pearl white, letter pressed, cotton business card.  I’m thinking maybe something with my initials on the front they will flip over for the rest of my information.  But don’t let that limit you.
The information I will have on the back of the business card will be my name, email, and phone number.
Some of the attributes that best describe me are: loyal, dependable, creative, risk taker, open minded, competitive, and empathetic.  I can adapt to my environment quickly and can get along with anyone.  I get excited by figuring out the way things work and finding solutions to problems.

Industry/Entity Type
Business

```html
<!DOCTYPE html>
<html lang="en">
<head>
<meta charset="utf-8">
<title>Daniel Whitcombe — Business Card</title>
<link rel="stylesheet" href="https://fonts.googleapis.com/css2?family=Cinzel:wght@400;600&display=swap">
<style>
  :root {
    --backdrop: #9b4a4c;
    --card-paper: #ececec;
    --ink-red: #8c1c1f;
  }
  * { margin: 0; padding: 0; box-sizing: border-box; }
  html, body {
    width: 1200px;
    height: 900px;
    overflow: hidden;
    background: var(--backdrop);
  }
  .canvas {
    width: 1200px;
    height: 900px;
    display: flex;
    align-items: center;
    justify-content: center;
    gap: 60px;
  }
  .card {
    width: 500px;
    height: 290px;
    background: var(--card-paper);
    border-radius: 16px;
    display: flex;
    flex-direction: column;
    align-items: center;
    justify-content: center;
    color: var(--ink-red);
    font-family: "Cinzel", serif;
  }
  .card-front .initials {
    font-size: 84px;
    font-weight: 400;
    letter-spacing: 2px;
    line-height: 1;
  }
  .card-back .holder-name {
    font-size: 25px;
    font-weight: 600;
    letter-spacing: 1px;
    line-height: 1.2;
  }
  .card-back .phone {
    font-size: 19px;
    font-weight: 400;
    letter-spacing: 1px;
    margin-top: 4px;
  }
  .card-back .rule {
    width: 300px;
    height: 1.5px;
    background: var(--ink-red);
    margin: 8px 0 6px;
  }
  .card-back .email {
    font-size: 15px;
    font-weight: 400;
    letter-spacing: 0.5px;
  }
</style>
</head>
<body>
  <main class="canvas">
    <section class="card card-front" aria-label="Card front">
      <div class="initials">DW</div>
    </section>
    <section class="card card-back" aria-label="Card back">
      <div class="holder-name">Daniel Whitcombe</div>
      <div class="phone">215-555-0142</div>
      <div class="rule"></div>
      <div class="email">DANIEL.WHITCOMBE@EXAMPLE.COM</div>
    </section>
  </main>
</body>
</html>
```